Professional, Scientific Cover Design for Nutritional / Hair Tissue Mineral Analysis (HTMA) Company

Hair tissue mineral analysis is a versatile, science-backed tool that offers a deeper understanding of your body's mineral and heavy metal profile. By evaluating long-term mineral balance and toxic exposures, HTMA provides invaluable insights that can aid in optimizing nutrition, addressing chronic health issues, and creating a personalized wellness strategy.

We have updated our logo and are in need of an updated report cover in which personalized test results are placed. We are looking for a professional and more modern look.

There are 2 small cutouts that will need to remain as shown in the picture in the brief.

Our updated logo along with color palette used will be uploaded in the brief as well as our 2 previous, outdated designs. We no longer want our address on the front cover. We also do not want images with people in them.

Thank you.

Website: www.pevdosk.com

Designs look the same

• Images with people

```html
<!DOCTYPE html>
<html lang="en">
<head>
<meta charset="UTF-8">
<title>Hair Tissue Mineral Analysis – Report Cover</title>
<link rel="stylesheet" href="https://fonts.googleapis.com/css2?family=Cinzel:wght@400;600&display=swap">
<style>
  :root {
    --page-bg: #d6d6d6;
    --cover-blue: #2b57a0;
    --cover-blue-deep: #1f4488;
    --mist-light: #dfe9f7;
    --mist-mid: #8fb0e0;
    --ember: #f08a2c;
    --text-white: #ffffff;
  }
  * { margin: 0; padding: 0; box-sizing: border-box; }
  html, body {
    width: 1200px;
    height: 1200px;
    overflow: hidden;
    background: var(--page-bg);
  }
  .report-cover {
    position: absolute;
    left: 211px;
    top: 50px;
    width: 778px;
    height: 1100px;
    background: var(--cover-blue);
    overflow: hidden;
    font-family: "Cinzel", "Times New Roman", serif;
    color: var(--text-white);
  }
  .cover-art {
    position: absolute;
    left: 0;
    top: 0;
    width: 100%;
    height: 790px;
    background:
      radial-gradient(ellipse 32% 18% at 47% 47%, rgba(240,138,44,0.75), rgba(240,138,44,0) 70%),
      radial-gradient(ellipse 75% 30% at 55% 52%, var(--mist-light), rgba(223,233,247,0) 70%),
      radial-gradient(ellipse 60% 40% at 30% 20%, rgba(143,176,224,0.8), rgba(143,176,224,0) 70%),
      radial-gradient(ellipse 50% 35% at 85% 30%, rgba(143,176,224,0.6), rgba(143,176,224,0) 70%),
      linear-gradient(180deg, #3c6cb5 0%, #325fa8 60%, var(--cover-blue) 100%);
  }
  .cover-art::after {
    content: "";
    position: absolute;
    left: 0;
    right: 0;
    bottom: 0;
    height: 220px;
    background: linear-gradient(180deg, rgba(43,87,160,0) 0%, var(--cover-blue) 100%);
  }
  .cover-title {
    position: absolute;
    left: 0;
    right: 0;
    top: 650px;
    text-align: center;
    font-weight: 400;
    line-height: 1;
    text-shadow: 0 2px 6px rgba(20,40,90,0.45);
  }
  .title-main {
    display: block;
    font-size: 82px;
    letter-spacing: 2px;
  }
  .title-sub {
    display: block;
    font-size: 54px;
    letter-spacing: 1px;
    margin-top: 16px;
    line-height: 1.28;
  }
  .title-rule {
    position: absolute;
    left: 123px;
    width: 532px;
    top: 917px;
    height: 5px;
    background: var(--ember);
  }
  .brand-mark {
    position: absolute;
    left: 0;
    right: 0;
    top: 978px;
    display: flex;
    align-items: center;
    justify-content: center;
    gap: 16px;
  }
  .brand-dot {
    width: 22px;
    height: 22px;
    border-radius: 50%;
    background: var(--ember);
  }
  .brand-name {
    font-size: 30px;
    font-weight: 600;
    letter-spacing: 1.5px;
    color: var(--text-white);
  }
</style>
</head>
<body>
  <main class="report-cover">
    <div class="cover-art" role="img" aria-label="Close-up scientific render of soft blue tissue strands with glowing orange mineral particles"></div>
    <h1 class="cover-title">
      <span class="title-main">Hair</span>
      <span class="title-sub">Tissue Mineral<br>Analysis</span>
    </h1>
    <div class="title-rule"></div>
    <div class="brand-mark">
      <span class="brand-dot"></span>
      <span class="brand-name">Corvane Research Labs, Inc.</span>
    </div>
  </main>
</body>
</html>
```